Can you design the Future of Mealworm Pet Food Packaging for me?

Project Overview:
We are seeking a dynamic and visually striking product label design for our range of mealworm pet food supplements. The label must effectively showcase the product, accommodate various container and packaging sizes, and include essential information such as a barcode, ingredients list, company address, and instructions for use. The design should exude positivity, capture the attention of consumers, and convey the quality and value of the product.

Target Audience:
Our target audience consists of health-conscious pet owners, aged 25-55, who prioritize quality, sustainability, and aesthetic appeal in their purchasing decisions. They are drawn to visually appealing packaging that conveys trustworthiness and authenticity.

Key Objectives:

Create a visually impactful label design that stands out on shelves and online platforms.
Clearly showcase the product while leaving space for essential information.
Ensure versatility to fit various container and packaging sizes.
Convey positivity, quality, and authenticity to resonate with our target audience.
Facilitate ease of use and readability for consumers.

Design Requirements:

Product Showcase: The label should prominently feature the product, with high-quality imagery, words or illustrations that highlight its key attributes and appeal to the target audience.

Space for Essential Information:
The design must include designated areas for a barcode, ingredients list, company address, and instructions for use. These elements should be clearly legible and easily accessible to consumers.

Versatility: The label design should be adaptable to different container shapes and sizes, including bottles, jars, and pouches. It should maintain its visual impact and readability across various packaging formats.

Positive Visual Impact: Incorporate colors, fonts, and imagery that evoke feelings of positivity, vitality, and well-being. Avoid clutter and maintain a clean, modern aesthetic. An example from a competitor company is attached for information.

To help provide you some focus, the first labels to be used in our production will measure 14cm x 6cm and the contents will weigh 20g

Please contact me if you have any questions about this brief or would like more info to help with your design. Thank you and I look forward to seeing your design.

Target Market(s)

Target Audience: Our target audience consists of health-conscious pet owners, aged 25-55, who prioritize quality, sustainability, and aesthetic appeal in their purchasing decisions. They are drawn to visually appealing packaging that conveys trustworthiness and authenticity.

Industry/Entity Type

Pet Food

Requirements
Must have
• Key Objectives: Create a visually impactful label design that stands out on shelves and online platforms. Clearly showcase the product while leaving space for essential information. Ensure versatility to fit various container and packaging sizes. Convey positivity, quality, and authenticity to resonate with our target audience. Facilitate ease of use and readability for consumers.
Nice to have
• Maintain a clean, modern aesthetic
Should not have
• Avoid clutter

```html
<!DOCTYPE html>
<html lang="en">
<head>
<meta charset="utf-8">
<title>Meal Worms – Goldfish Flakes Label</title>
<link rel="stylesheet" href="https://fonts.googleapis.com/css2?family=Playfair+Display:wght@900&family=Montserrat:wght@300;500&family=Open+Sans:wght@700&family=Fira+Sans+Condensed:wght@400&family=Oswald:wght@400&display=swap">
<style>
  :root {
    --page: #ffffff;
    --red: #c2432f;
    --red-light: #d9604c;
    --black: #050505;
    --yellow: #d6a90b;
    --green: #5f7b55;
    --white: #ffffff;
    --text-yellow: #e8b913;
    --fish-orange: #f08a2a;
    --fish-light: #f7c470;
    --worm-brown: #8a6a3f;
    --worm-light: #c4a577;
  }
  * { margin: 0; padding: 0; box-sizing: border-box; }
  html, body { width: 1200px; height: 867px; overflow: hidden; background: var(--page); }
  .label {
    position: absolute; left: 240px; top: 126px;
    width: 720px; height: 615px; overflow: hidden;
  }
  .label-shapes { position: absolute; inset: 0; }
  .badge {
    position: absolute; width: 130px; text-align: center;
    font-family: "Open Sans", sans-serif; font-weight: 700;
    font-size: 15px; line-height: 18px; color: var(--white);
  }
  .badge svg { display: block; margin: 0 auto 6px; }
  .badge--kelp { left: 37px; top: 33px; }
  .badge--harvest { left: 219px; top: 33px; }
  .brand {
    position: absolute; left: 380px; top: 135px; width: 320px; text-align: center;
    color: var(--white);
  }
  .brand-name {
    font-family: "Playfair Display", serif; font-weight: 900;
    font-size: 68px; line-height: 72px; letter-spacing: 3px;
  }
  .brand-tagline {
    font-family: "Montserrat", sans-serif; font-weight: 500;
    font-size: 20px; letter-spacing: 1.5px; margin-top: 2px;
  }
  .fish-art {
    position: absolute; left: 30px; top: 140px; width: 330px; height: 260px;
    border-radius: 50% 45% 50% 40%;
    background: radial-gradient(ellipse at 65% 50%, var(--fish-orange), var(--fish-light) 60%, rgba(247,196,112,0) 72%);
  }
  .product-name {
    position: absolute; left: 36px; top: 404px; color: var(--white);
  }
  .product-title {
    font-family: "Playfair Display", serif; font-weight: 900;
    font-size: 50px; line-height: 56px; letter-spacing: 1px;
  }
  .product-sub {
    font-family: "Montserrat", sans-serif; font-weight: 300;
    font-size: 40px; line-height: 44px;
  }
  .product-desc {
    position: absolute; left: 36px; top: 518px; width: 330px;
    font-family: "Fira Sans Condensed", sans-serif; font-size: 20px; line-height: 24px;
    color: var(--text-yellow);
  }
  .variety {
    position: absolute; left: 423px; top: 272px;
    font-family: "Playfair Display", serif; font-weight: 900;
    font-size: 64px; line-height: 64px; letter-spacing: 2px; color: var(--white);
  }
  .worm-art {
    position: absolute; left: 440px; top: 418px; width: 238px; height: 126px;
    border-radius: 50%;
    background: radial-gradient(ellipse at center, var(--worm-brown), var(--worm-light) 55%, rgba(196,165,119,0) 72%);
  }
  .net-weight {
    position: absolute; left: 400px; top: 552px; width: 320px; height: 63px;
    display: flex; align-items: center; justify-content: center;
    font-family: "Oswald", sans-serif; font-size: 22px; color: var(--white);
  }
</style>
</head>
<body>
  <main class="label">
    <svg class="label-shapes" width="720" height="615" viewBox="0 0 720 615" aria-hidden="true">
      <defs>
        <linearGradient id="red-band" x1="0" y1="0" x2="1" y2="0">
          <stop offset="0" stop-color="var(--red-light)"/>
          <stop offset="1" stop-color="var(--red)"/>
        </linearGradient>
      </defs>
      <rect x="0" y="0" width="720" height="260" fill="url(#red-band)"/>
      <rect x="390" y="258" width="330" height="296" fill="var(--yellow)"/>
      <rect x="390" y="552" width="330" height="63" fill="var(--green)"/>
      <polygon fill="var(--black)" points="0,258 392,258 392,290 400,300 393,318 400,335 390,350 396,372 385,392 380,402 372,420 378,438 366,452 376,470 372,490 384,505 392,525 395,552 410,570 416,615 0,615"/>
    </svg>

    <div class="badge badge--kelp">
      <svg width="78" height="78" viewBox="0 0 78 78" aria-hidden="true">
        <circle cx="39" cy="39" r="36" fill="none" stroke="var(--white)" stroke-width="3"/>
        <path d="M39 62 V40 M39 46 L28 32 M39 42 L50 28 M28 32 L24 24 M28 32 L34 22 M50 28 L46 20 M50 28 L56 22" stroke="var(--white)" stroke-width="3.5" fill="none" stroke-linecap="round"/>
      </svg>
      WITH<br>SEA KELP
    </div>
    <div class="badge badge--harvest">
      <svg width="78" height="78" viewBox="0 0 78 78" aria-hidden="true">
        <circle cx="39" cy="39" r="36" fill="none" stroke="var(--white)" stroke-width="3"/>
        <path d="M18 42 C26 24 48 20 60 28 C50 30 40 36 34 44 Z" fill="var(--white)"/>
        <path d="M60 36 C52 54 30 58 18 50 C28 48 38 42 44 34 Z" fill="var(--white)"/>
      </svg>
      SUSTAINABLY<br>HARVESTED
    </div>

    <div class="brand">
      <div class="brand-name">BRAND</div>
      <div class="brand-tagline">Premium Pet Foods</div>
    </div>

    <div class="fish-art" role="img" aria-label="Illustration of an orange goldfish swimming to the right"></div>

    <div class="product-name">
      <div class="product-title">GOLDFISH</div>
      <div class="product-sub">FLAKES</div>
    </div>
    <p class="product-desc">Natural food, crammed with goodness for all coldwater fish, with no artificial colors</p>

    <h1 class="variety">MEAL<br>WORMS</h1>
    <div class="worm-art" role="img" aria-label="Photo of a pile of dried mealworms"></div>

    <div class="net-weight">NET WEIGHT 20g (0.7oz)</div>
  </main>
</body>
</html>
```